3 Business Card designs for a company with multiple services

We are a company that has 3 main services:

1) Security - CCTV & Alarm Sepcialists
2) Broadcast - Broadcast Sales and Technical Services
3) Distribution - Quality Products, Quality Service

The broadcast service is for Video Broadcast.

I will include our logos for each service.

I would like to also create a business card design for 7QK in general (see main logo).

Each card will be two-sided. On the front I would think it would include Logo, Name, Posistion and Mobile (and possibly email). And possibly our main number (which may be something like 1800 639 415)

On the back it MUST include a "lined" section to be able to write short quotes / prices.

Then include more details like Phone: 1800 639 415 Fax: 1800 639 412 Postal: PO Box 731, Tallowen, QLD Australia 4290 Website: www.7qk.com.au

We would like a fresh, inovative card design with that "wow check this out" feel about it.

Look forward to seeing what you can do! :)

Corey

Industry/Entity Type

Business

Requirements
Must have
• Quote section on the back!
Editable files.

```html
<!DOCTYPE html>
<html lang="en">
<head>
<meta charset="utf-8">
<title>7QK Business Cards</title>
<link rel="stylesheet" href="https://fonts.googleapis.com/css2?family=Arimo:wght@400;700&display=swap">
<style>
:root{
  --ink:#333333;
  --bar:#353535;
  --text:#2b2b2b;
  --label:#555555;
  --rule:#555555;
  --paper:#ffffff;
  --general:#353535;
  --security:#8c8c8c;
  --broadcast:#e38c00;
  --distribution:#1d3b82;
  --security-mark:#c8202a;
  --broadcast-mark:#f2b61c;
  --distribution-mark:#2f6fbf;
  --general-mark:#8a8a8a;
}
*{box-sizing:border-box;margin:0;padding:0}
html,body{width:848px;height:1200px;overflow:hidden;background:var(--paper)}
body{position:relative;font-family:Arimo,Helvetica,Arial,sans-serif;color:var(--text)}
.card{position:absolute;width:374px;height:222px;border:1px solid #222;background:var(--paper);overflow:hidden}
.col-front{left:41px}
.col-back{left:437px}
.row-1{top:75px}.row-2{top:321px}.row-3{top:569px}.row-4{top:817px}

.logo{position:absolute;left:13px;top:13px;height:34px;width:113px;background:var(--bar);border-radius:5px 0 0 0;display:flex;align-items:center;gap:8px;padding-left:6px}
.card.general .logo{width:152px}
.logo .dot{width:20px;height:20px;border-radius:50%;background:var(--mark)}
.logo .wordmark{color:#fff;font-weight:700;font-size:20px;letter-spacing:6px}

.namebar{position:absolute;left:130px;right:0;top:13px;height:23px;background:var(--bar);color:#fff;font-weight:700;font-size:14px;line-height:23px;padding-left:6px}
.subband{position:absolute;left:130px;right:0;top:36px;height:11px;background:var(--band);color:#fff;font-size:9.5px;line-height:11px;padding-left:6px}
.card.general .namebar,.card.general .subband{left:171px}
.card.general .subband{border-top:1px solid #fff}

.contact{position:absolute;left:126px;top:66px;height:106px;border-left:1.5px solid var(--rule);padding-left:6px;font-size:10.5px;line-height:14px}
.card.general .contact{left:170px;top:63px;height:145px}
.contact .postal{margin-bottom:12px}
.contact dl{display:grid;grid-template-columns:44px auto;line-height:14.7px}
.contact dt{font-weight:700;color:var(--label)}

.quote-title{position:absolute;left:137px;top:13px;height:23px;line-height:23px;color:#fff;font-weight:700;font-size:13px}
.card.general .quote-title{left:175px}
.date-box{position:absolute;left:234px;top:15px;width:127px;height:18px;background:#fff;border-radius:3px;font-size:10px;line-height:18px;padding-left:4px;color:var(--text)}
.quote-lines{position:absolute;left:12px;right:12px;top:77px}
.quote-lines span{display:block;height:1.5px;background:var(--rule);margin-bottom:31.5px}

.general{--band:var(--general);--mark:var(--general-mark)}
.security{--band:var(--security);--mark:var(--security-mark)}
.broadcast{--band:var(--broadcast);--mark:var(--broadcast-mark)}
.distribution{--band:var(--distribution);--mark:var(--distribution-mark)}
</style>
</head>
<body>

<!-- General -->
<section class="card col-front row-1 general">
  <div class="logo"><span class="dot"></span><span class="wordmark">7QK</span></div>
  <div class="namebar">Grant Ellison</div>
  <div class="subband">Managing Director</div>
  <div class="contact">
    <p class="postal">PO Box 731,<br>Tallowen, QLD 4290</p>
    <dl><dt>Tel.</dt><dd>1800 639 415</dd><dt>Fax.</dt><dd>1800 639 412</dd><dt>Mobile.</dt><dd>0438 917 205</dd><dt>Email.</dt><dd>grant@7qk.com.au</dd><dt>Web.</dt><dd>www.7qk.com.au</dd></dl>
  </div>
</section>
<section class="card col-back row-1 general">
  <div class="logo"><span class="dot"></span><span class="wordmark">7QK</span></div>
  <div class="namebar"></div><div class="subband"></div>
  <div class="quote-title">QUOTE ...</div>
  <div class="date-box">Date: ____ / ____ /______</div>
  <div class="quote-lines"><span></span><span></span><span></span><span></span><span></span></div>
</section>

<!-- Security -->
<section class="card col-front row-2 security">
  <div class="logo"><span class="dot"></span><span class="wordmark">7QK</span></div>
  <div class="namebar">Nathan Brierley</div>
  <div class="subband">CCTV and Alarm Specialist</div>
  <div class="contact">
    <p class="postal">PO Box 731,<br>Tallowen, QLD 4290</p>
    <dl><dt>Tel.</dt><dd>1800 639 415</dd><dt>Fax.</dt><dd>1800 639 412</dd><dt>Mobile.</dt><dd>0438 917 205</dd><dt>Email.</dt><dd>nathan@7qk.com.au</dd><dt>Web.</dt><dd>www.7qk.com.au</dd></dl>
  </div>
</section>
<section class="card col-back row-2 security">
  <div class="logo"><span class="dot"></span><span class="wordmark">7QK</span></div>
  <div class="namebar"></div><div class="subband"></div>
  <div class="quote-title">QUOTE ...</div>
  <div class="date-box">Date: ____ / ____ /______</div>
  <div class="quote-lines"><span></span><span></span><span></span><span></span><span></span></div>
</section>

<!-- Broadcast -->
<section class="card col-front row-3 broadcast">
  <div class="logo"><span class="dot"></span><span class="wordmark">7QK</span></div>
  <div class="namebar">Simon Hartley</div>
  <div class="subband">Sales and Technical Services</div>
  <div class="contact">
    <p class="postal">PO Box 731,<br>Tallowen, QLD 4290</p>
    <dl><dt>Tel.</dt><dd>1800 639 415</dd><dt>Fax.</dt><dd>1800 639 412</dd><dt>Mobile.</dt><dd>0438 917 205</dd><dt>Email.</dt><dd>simon@7qk.com.au</dd><dt>Web.</dt><dd>www.7qk.com.au</dd></dl>
  </div>
</section>
<section class="card col-back row-3 broadcast">
  <div class="logo"><span class="dot"></span><span class="wordmark">7QK</span></div>
  <div class="namebar"></div><div class="subband"></div>
  <div class="quote-title">QUOTE ...</div>
  <div class="date-box">Date: ____ / ____ /______</div>
  <div class="quote-lines"><span></span><span></span><span></span><span></span><span></span></div>
</section>

<!-- Distribution -->
<section class="card col-front row-4 distribution">
  <div class="logo"><span class="dot"></span><span class="wordmark">7QK</span></div>
  <div class="namebar">Darren Kellett</div>
  <div class="subband">Distribution Specialist</div>
  <div class="contact">
    <p class="postal">PO Box 731,<br>Tallowen, QLD 4290</p>
    <dl><dt>Tel.</dt><dd>1800 639 415</dd><dt>Fax.</dt><dd>1800 639 412</dd><dt>Mobile.</dt><dd>0438 917 205</dd><dt>Email.</dt><dd>darren@7qk.com.au</dd><dt>Web.</dt><dd>www.7qk.com.au</dd></dl>
  </div>
</section>
<section class="card col-back row-4 distribution">
  <div class="logo"><span class="dot"></span><span class="wordmark">7QK</span></div>
  <div class="namebar"></div><div class="subband"></div>
  <div class="quote-title">QUOTE ...</div>
  <div class="date-box">Date:____ /____ /______</div>
  <div class="quote-lines"><span></span><span></span><span></span><span></span><span></span></div>
</section>

</body>
</html>
```